International Freight Forwarder need a business card

We need a logo design for a freight forwarding company . We are active in Sea Transportation, Truck transportation, and Air Transportation, The design should be have normal dimensions of a card and should not have cuts and holes in its design (printed design is required - lamination accepted)

The said company is agent and sales representative of 2 other Shipping companies (whose logos, name, and website should also be mentioned on the card)

Industry/Entity Type

Logistics

Contact Information for Business Card

Address is "No.7, 2nd Sarv Baghestan-e-Nouri, Tehran, IR
Tel number is +98 21 66394512
Fax number is +98 21 66395830
E-Mail address is info@roshanbarsaz.com
Website is www.roshanbarsaz.com

Open Layer Logos attached as well

Colors
33a6d7
0292cd
0255a3
3276b5
85abd2
85cae6
cee9f5
d5e2ee
ffffff

Requirements
Must have
• Main logo of Roshan Barsaz
• Logo of TQM Shipping Line
• London, United Kingdom
• tqmline.com
• Logo of Calm Reef Shipping
• Dubai, United Arab Emirates
• crsuae.com
• We require OPEN layer file to be submitted to us upon project selection.
Should not have
• Weird Designs such as cuts to the shape or holes in design.

```html
<!DOCTYPE html>
<html lang="en">
<head>
<meta charset="utf-8">
<title>Roshan Barsaz International Transport – Business Card</title>
<link href="https://fonts.googleapis.com/css2?family=Open+Sans:wght@400;600&display=swap" rel="stylesheet">
<style>
  :root{
    --navy:#1f2a7a;
    --royal:#0255a3;
    --sky:#33a6d7;
    --cyan:#0292cd;
    --steel:#3276b5;
    --mist:#85abd2;
    --ice:#cee9f5;
    --white:#ffffff;
    --ink:#333a44;
    --stage:#e6eaee;
  }
  *{box-sizing:border-box;margin:0;padding:0}
  html,body{width:1200px;height:1000px;overflow:hidden}
  body{background:var(--stage);font-family:"Open Sans",Arial,sans-serif;position:relative}
  .card{position:absolute;left:250px;width:700px;height:400px;border-radius:18px;overflow:hidden;box-shadow:0 8px 24px rgba(0,0,0,.18)}
  .card--front{top:60px;background:linear-gradient(160deg,#ffffff 0%,#f4f5f6 55%,#e9ebed 100%)}
  .card--back{top:540px;background:radial-gradient(ellipse at 65% 35%,#1f86c9 0%,#1371b5 45%,#0a4f8c 100%)}
  .holder{position:absolute;left:48px;top:40px}
  .holder__name{font-size:26px;font-weight:600;color:var(--navy);letter-spacing:.5px}
  .holder__role{font-size:17px;color:var(--ink);margin-top:2px}
  .address{position:absolute;left:48px;top:150px;font-size:16px;line-height:24px;color:var(--ink)}
  .contacts{position:absolute;left:48px;top:212px;list-style:none;font-size:16px;color:var(--ink)}
  .contacts li{display:flex;align-items:center;height:24px}
  .contacts svg{width:17px;height:17px;margin-right:10px;flex:none}
  .swoosh{position:absolute;left:0;bottom:0;width:700px;height:400px}
  .brand{position:absolute;display:flex;align-items:center;gap:14px}
  .brand--front{right:40px;top:150px}
  .brand__mark{border-radius:50%;flex:none}
  .brand--front .brand__mark{width:90px;height:90px;border:3px solid var(--mist)}
  .brand__name{font-size:17px;font-weight:600;color:var(--royal);line-height:21px}
  .partner{position:absolute;display:flex;align-items:center;gap:10px}
  .partner--front{right:40px;bottom:26px}
  .partner--front .partner__mark{width:44px;height:44px;border-radius:50%;background:var(--royal)}
  .partner--front .partner__name{font-size:15px;font-weight:600;color:var(--white);line-height:18px}
  .brand--back{left:170px;top:110px;gap:26px}
  .brand--back .brand__mark{width:150px;height:150px;border:4px solid var(--ice)}
  .brand--back .brand__name{font-size:28px;color:var(--ice);line-height:36px;font-weight:400}
  .partner--back{right:60px;bottom:40px}
  .partner--back .partner__mark{width:40px;height:40px;border-radius:50%;border:2px solid var(--ice)}
  .partner--back .partner__name{font-size:15px;color:var(--ice);line-height:18px;font-weight:400}
</style>
</head>
<body>
  <section class="card card--front" aria-label="Card front">
    <svg class="swoosh" viewBox="0 0 700 400" aria-hidden="true">
      <path d="M0 330 C 200 345, 420 365, 700 400 L 0 400 Z" fill="var(--cyan)"/>
      <path d="M0 318 C 200 332, 420 352, 700 385 L 700 400 C 420 365, 200 345, 0 330 Z" fill="var(--ice)"/>
      <path d="M360 400 C 460 372, 560 364, 700 360 L 700 400 Z" fill="var(--sky)"/>
    </svg>

    <div class="holder">
      <p class="holder__name">DARIAN HOLT</p>
      <p class="holder__role">Executive</p>
    </div>

    <p class="address">No.7, 2nd Sarv<br>Baghestan-e-Nouri, Tehran, IR</p>

    <ul class="contacts">
      <li><svg viewBox="0 0 20 20"><circle cx="10" cy="10" r="10" fill="var(--steel)"/><path d="M6.5 5.5l2 0 1 2.5-1.2.9a6 6 0 0 0 2.8 2.8l.9-1.2 2.5 1v2c0 .6-.5 1-1 1A8.5 8.5 0 0 1 5.5 6.5c0-.5.4-1 1-1z" fill="#fff"/></svg>+98 21 66394512</li>
      <li><svg viewBox="0 0 20 20"><circle cx="10" cy="10" r="10" fill="var(--steel)"/><rect x="7" y="5" width="6" height="3" fill="#fff"/><rect x="5" y="8" width="10" height="5" rx="1" fill="#fff"/><rect x="7" y="12" width="6" height="3" fill="#fff"/></svg>+98 21 66395830</li>
      <li><svg viewBox="0 0 20 20"><circle cx="10" cy="10" r="10" fill="var(--steel)"/><rect x="5" y="6.5" width="10" height="7" fill="#fff"/><path d="M5 6.5l5 4 5-4" fill="none" stroke="var(--steel)" stroke-width="1"/></svg>info@roshanbarsaz.com</li>
      <li><svg viewBox="0 0 20 20"><circle cx="10" cy="10" r="10" fill="var(--steel)"/><circle cx="9" cy="9" r="3.5" fill="none" stroke="#fff" stroke-width="1.6"/><path d="M11.5 11.5l3 3" stroke="#fff" stroke-width="1.8"/></svg>www.roshanbarsaz.com</li>
    </ul>

    <div class="brand brand--front">
      <span class="brand__mark"></span>
      <p class="brand__name">Roshan Barsaz<br>International<br>Transport.Co L.Lc</p>
    </div>

    <div class="partner partner--front">
      <span class="partner__mark"></span>
      <p class="partner__name">Calm Reef<br>Shipping LLC</p>
    </div>
  </section>

  <section class="card card--back" aria-label="Card back">
    <div class="brand brand--back">
      <span class="brand__mark"></span>
      <p class="brand__name">Roshan Barsaz<br>International<br>Transport.Co L.Lc</p>
    </div>
    <div class="partner partner--back">
      <span class="partner__mark"></span>
      <p class="partner__name">TQM<br>Shipping Line Ltd</p>
    </div>
  </section>
</body>
</html>
```